Larkfield civic consultancy needs a business card design

Business card should represent civil engineering infrastructure projects such as roads, bridges, tunnels, rail, rail, pipelines, structures and resource infrastructure

```html
<!DOCTYPE html>
<html lang="en">
<head>
<meta charset="utf-8">
<title>Larkfield civic consultancy – Business card</title>
<link rel="stylesheet" href="https://fonts.googleapis.com/css2?family=Archivo:wght@700;800&family=Archivo+Narrow:wght@700&display=swap">
<style>
  :root {
    --card-bg: #fff9f6;
    --brand-blue: #0022cc;
    --brand-gold: #c8901e;
    --ink: #0a0a12;
  }
  html, body {
    margin: 0;
    padding: 0;
    overflow: hidden;
    background: var(--card-bg);
  }
  .card {
    position: relative;
    width: 1200px;
    height: 676px;
    background: var(--card-bg);
    overflow: hidden;
  }
  .brand-mark {
    position: absolute;
    left: 150px;
    top: 80px;
    width: 170px;
    height: 170px;
    border-radius: 50%;
    background: var(--brand-gold);
  }
  .brand-name {
    position: absolute;
    left: 372px;
    top: 62px;
    margin: 0;
    font-family: "Archivo", sans-serif;
    font-weight: 800;
    font-size: 170px;
    line-height: 1;
    letter-spacing: 2px;
    color: var(--brand-blue);
  }
  .person-name {
    position: absolute;
    left: 120px;
    top: 352px;
    margin: 0;
    font-family: "Archivo", sans-serif;
    font-weight: 700;
    font-size: 52px;
    line-height: 1;
    color: var(--ink);
  }
  .contact-list {
    position: absolute;
    left: 354px;
    top: 456px;
    margin: 0;
    padding: 0;
    list-style: none;
    font-family: "Archivo Narrow", sans-serif;
    font-weight: 700;
    font-size: 40px;
    line-height: 57px;
    color: var(--ink);
  }
</style>
</head>
<body>
  <main class="card">
    <div class="brand-mark" aria-hidden="true"></div>
    <p class="brand-name">LCC</p>

    <h1 class="person-name">Daniel Hartley</h1>

    <ul class="contact-list">
      <li class="contact-phone">Mobile: +61400123456</li>
      <li class="contact-email">daniel.hartley@larkfieldcivic.com.au</li>
      <li class="contact-email">daniel.j.hartley@harbourmail.com</li>
    </ul>
  </main>
</body>
</html>
```